Q-Rolls Business Card

We are a modern retail clothing store. Established in 1994. I need a presentable card that will amaze vendors when given to them.

Front: Logo in middle
Info Side:

Name: Tomas Velder
Cell: 630-812-4463
Work: 630-917-3384 EXT. 417
Email: Tomas@q-rolls-example.com
Website: www.Q-rolls-example.com

Industry/Entity Type

Business

```html
<!DOCTYPE html>
<html lang="en">
<head>
<meta charset="utf-8">
<title>Q-Rolls Business Card</title>
<link rel="stylesheet" href="https://fonts.googleapis.com/css2?family=Exo+2:wght@700&family=Arimo:wght@400;700&display=swap">
<style>
  :root {
    --stage: #e9e7e3;
    --card-black: #0b0b0b;
    --card-white: #ffffff;
    --ink: #111111;
    --muted: #9a9a9a;
    --logo: #ffffff;
    --rule: #8c8c8c;
  }
  * { margin: 0; padding: 0; box-sizing: border-box; }
  html, body { width: 1200px; height: 950px; overflow: hidden; }
  body {
    background: var(--stage);
    font-family: "Arimo", Arial, sans-serif;
    position: relative;
  }
  .card {
    position: absolute;
    left: 320px;
    width: 560px;
    height: 320px;
    overflow: hidden;
    box-shadow: 0 14px 30px rgba(0,0,0,0.25);
  }
  /* Front */
  .card--front {
    top: 110px;
    background: var(--card-black);
  }
  .front__logo {
    position: absolute;
    top: 108px;
    left: 0; right: 0;
    text-align: center;
    font-family: "Exo 2", Arial, sans-serif;
    font-weight: 700;
    font-size: 62px;
    color: var(--logo);
    letter-spacing: 2px;
  }
  .front__web {
    position: absolute;
    top: 196px;
    left: 0; right: 0;
    display: flex;
    align-items: center;
    justify-content: center;
    gap: 14px;
    color: #cfcfcf;
    font-size: 13px;
    letter-spacing: 5px;
  }
  .front__rule {
    width: 90px;
    height: 1px;
    background: linear-gradient(90deg, transparent, var(--rule));
  }
  .front__rule--right { background: linear-gradient(90deg, var(--rule), transparent); }
  /* Back */
  .card--back {
    top: 520px;
    background: var(--card-white);
  }
  .back__band {
    position: absolute;
    top: 0; left: 0; right: 0;
    height: 200px;
    background: var(--card-black);
  }
  .back__logo {
    position: absolute;
    top: 62px;
    left: 0; right: 0;
    text-align: center;
    font-family: "Exo 2", Arial, sans-serif;
    font-weight: 700;
    font-size: 74px;
    color: var(--logo);
    letter-spacing: 3px;
  }
  .back__info {
    position: absolute;
    top: 216px;
    left: 26px;
    right: 22px;
    bottom: 16px;
    display: flex;
    justify-content: space-between;
    color: var(--ink);
    font-size: 13px;
  }
  .person__name {
    font-weight: 700;
    font-size: 15px;
    text-transform: uppercase;
  }
  .person__title {
    margin-top: 3px;
    color: var(--muted);
    font-size: 13px;
  }
  .contact { list-style: none; }
  .contact li {
    display: flex;
    align-items: center;
    gap: 7px;
    margin-bottom: 6px;
  }
  .contact--web { align-self: flex-end; }
  .icon { width: 13px; height: 13px; fill: var(--ink); flex: none; }
</style>
</head>
<body>
  <section class="card card--front" aria-label="Card front">
    <div class="front__logo">Q-ROLLS</div>
    <div class="front__web">
      <span class="front__rule"></span>
      <span>www.q-rolls-example.com</span>
      <span class="front__rule front__rule--right"></span>
    </div>
  </section>

  <section class="card card--back" aria-label="Card back">
    <div class="back__band">
      <div class="back__logo">Q-ROLLS</div>
    </div>
    <div class="back__info">
      <div class="person">
        <div class="person__name">Tomas Velder</div>
        <div class="person__title">CEO/FOUNDER</div>
      </div>
      <ul class="contact contact--phone">
        <li>
          <svg class="icon" viewBox="0 0 13 13" aria-hidden="true"><rect x="3" y="0" width="7" height="13" rx="1.5"/><rect x="4.3" y="1.6" width="4.4" height="8" fill="#fff"/></svg>
          630-812-4463
        </li>
        <li>
          <svg class="icon" viewBox="0 0 13 13" aria-hidden="true"><path d="M0 4 Q6.5 0 13 4 L11 6 L9 4.5 L4 4.5 L2 6 Z"/><rect x="2" y="7" width="9" height="5" rx="1"/></svg>
          630-917-3384 EXT. 417
        </li>
      </ul>
      <ul class="contact contact--web">
        <li>
          <svg class="icon" viewBox="0 0 13 13" aria-hidden="true"><rect x="0" y="2" width="13" height="9"/><path d="M0.5 2.5 L6.5 7 L12.5 2.5" stroke="#fff" stroke-width="1.2" fill="none"/></svg>
          Tomas@q-rolls-example.com
        </li>
        <li>
          <svg class="icon" viewBox="0 0 13 13" aria-hidden="true"><circle cx="6.5" cy="6.5" r="6.5"/><path d="M0.5 6.5 H12.5 M6.5 0.5 C3.5 4 3.5 9 6.5 12.5 M6.5 0.5 C9.5 4 9.5 9 6.5 12.5" stroke="#fff" stroke-width="0.9" fill="none"/></svg>
          www.Q-rolls-example.com
        </li>
      </ul>
    </div>
  </section>
</body>
</html>
```